Business Card and Logo Color Scheme Design Contest

We are starting a new company called Lone Ridge Structural Partners and already have a logo however, the colors for the logo itself are not final and COULD be changed. I'm hoping to move AWAYfrom the gold color in the card and the logo as it seems a bit outdated. What we need help with is to find what our business color scheme will be, and then incorporate those colors into both the logo and the business card design itself. We also want to make sure we are known as "LRS" so in the future we can just refer to ourselves as "LRS" and not Lone Ridge Structural Partners. That being said, I would like to make a slight change to the logo to somehow include the letters "LRS." The logo used in the front of the card design MUST ALSO include the words "Firm No. 64307" within the logo. My vision is for the front of the card to have the information shown in the attached image. For the back of the card, I'm hoping to have something very simple. I'm envisioning a solid color with either the website (www.bridgemarkplans.com) and a simplified version of the logo. I've attached an example but I'm looking for a complete redesign. I'm looking for a slick, modern and simple design.

Industry/Entity Type

Civil Engineer

Contact Information for Business Card

Logo
Firm No. 64307
Dalton Whitmere, PE
Chief Operating Officer
Email:dwhitmere@bridgemarkplans.com
Ph: 936.555.0142 | D: 936.555.0178 | M:210.555.0263
4187 W. Kellingham, Conroe, Texas 77301
www.bridgemarkplans.com

Requirements
Must have
• Logo
Contact Info
Nice to have
• "LRS" Incorporated in the design
Should not have
• The current color scheme

```html
<!DOCTYPE html>
<html lang="en">
<head>
<meta charset="utf-8">
<title>Lone Ridge Structural Partners – Business Card</title>
<link rel="stylesheet" href="https://fonts.googleapis.com/css2?family=Tinos:wght@400;700&family=Montserrat:wght@600;700&family=Open+Sans:wght@400&display=swap">
<style>
  :root {
    --stage: #2b2b2b;
    --stone: #c8bfae;
    --paper: #ffffff;
    --ink: #1f1f1f;
    --navy: #2b3a8c;
    --brick: #9a1f1f;
    --mark-fill: #c8bfae;
  }
  * { margin: 0; padding: 0; box-sizing: border-box; }
  html, body { width: 1200px; height: 900px; overflow: hidden; }
  body { background: var(--stage); position: relative; }

  .card { position: absolute; width: 560px; height: 320px; box-shadow: 0 10px 28px rgba(0,0,0,.45); }

  /* Back of card */
  .card-back { left: 90px; top: 90px; background: var(--stone); }
  .card-back .brand { position: absolute; left: 0; right: 0; top: 92px; display: flex; justify-content: center; align-items: center; gap: 14px; }
  .brand-square { width: 22px; height: 22px; background: var(--ink); }
  .brand-name { font-family: "Tinos", serif; font-weight: 700; font-size: 56px; letter-spacing: 2px; color: var(--ink); line-height: 1; }
  .firm-no { font-family: "Tinos", serif; font-weight: 700; font-size: 12px; color: var(--ink); }
  .card-back .firm-no { position: absolute; left: 0; right: 0; top: 168px; text-align: center; }
  .card-back .site { position: absolute; left: 0; right: 0; bottom: 42px; text-align: center; font-family: "Tinos", serif; font-weight: 700; font-size: 21px; letter-spacing: 1.5px; color: var(--ink); }

  /* Front of card */
  .card-front { left: 550px; top: 480px; background: var(--paper); }
  .card-front .brand { position: absolute; right: 48px; top: 34px; display: flex; align-items: center; gap: 12px; }
  .card-front .brand-name { font-size: 46px; }
  .card-front .brand-square { width: 18px; height: 18px; background: var(--mark-fill); }
  .card-front .firm-no { position: absolute; right: 52px; top: 96px; }

  .person { position: absolute; left: 40px; top: 128px; }
  .person-name { font-family: "Montserrat", sans-serif; font-weight: 700; font-size: 30px; color: var(--navy); line-height: 1.1; }
  .person-title { font-family: "Open Sans", sans-serif; font-size: 18px; color: var(--brick); margin-top: 2px; }

  .contact-list { position: absolute; left: 40px; top: 208px; list-style: none; }
  .contact-list li { display: flex; align-items: center; gap: 10px; font-family: "Open Sans", sans-serif; font-size: 15px; color: var(--ink); line-height: 22px; white-space: nowrap; }
  .contact-list svg { width: 13px; height: 13px; fill: var(--navy); flex: none; }
</style>
</head>
<body>

<section class="card card-back" aria-label="Back of business card">
  <div class="brand">
    <span class="brand-square"></span>
    <span class="brand-name">LRS</span>
  </div>
  <p class="firm-no">Firm No. 64307</p>
  <p class="site">WWW.BRIDGEMARKPLANS.COM</p>
</section>

<section class="card card-front" aria-label="Front of business card">
  <div class="brand">
    <span class="brand-square"></span>
    <span class="brand-name">LRS</span>
  </div>
  <p class="firm-no">Firm No. 64307</p>

  <div class="person">
    <h1 class="person-name">Dalton Whitmere, PE</h1>
    <p class="person-title">Chief Operating Officer</p>
  </div>

  <ul class="contact-list">
    <li>
      <svg viewBox="0 0 24 24" aria-hidden="true"><path d="M6.6 10.8a15.1 15.1 0 0 0 6.6 6.6l2.2-2.2a1 1 0 0 1 1-.25 11.4 11.4 0 0 0 3.6.57 1 1 0 0 1 1 1V20a1 1 0 0 1-1 1A17 17 0 0 1 3 4a1 1 0 0 1 1-1h3.5a1 1 0 0 1 1 1c0 1.25.2 2.45.57 3.57a1 1 0 0 1-.25 1z"/></svg>
      Ph: 936.555.0142 | D: 936.555.0178 | M:210.555.0263
    </li>
    <li>
      <svg viewBox="0 0 24 24" aria-hidden="true"><path d="M2 5h20v14H2z M2 5l10 8 10-8" /></svg>
      dwhitmere@bridgemarkplans.com
    </li>
    <li>
      <svg viewBox="0 0 24 24" aria-hidden="true"><path d="M12 2a10 10 0 1 0 0 20 10 10 0 0 0 0-20zm0 2c.9 1.2 1.6 2.8 1.9 5h-3.8c.3-2.2 1-3.8 1.9-5zM4.3 10h3.8a17 17 0 0 0 0 4H4.3a8 8 0 0 1 0-4zm5.8 0h3.8a15 15 0 0 1 0 4h-3.8a15 15 0 0 1 0-4zm5.8 0h3.8a8 8 0 0 1 0 4h-3.8a17 17 0 0 0 0-4zM12 20c-.9-1.2-1.6-2.8-1.9-5h3.8c-.3 2.2-1 3.8-1.9 5z"/></svg>
      www.bridgemarkplans.com
    </li>
    <li>
      <svg viewBox="0 0 24 24" aria-hidden="true"><path d="M12 2a7 7 0 0 0-7 7c0 5.2 7 13 7 13s7-7.8 7-13a7 7 0 0 0-7-7zm0 9.5a2.5 2.5 0 1 1 0-5 2.5 2.5 0 0 1 0 5z"/></svg>
      4187 W. Kellingham, Conroe, Texas 77301
    </li>
  </ul>
</section>

</body>
</html>
```